tourism marketplace web app redesign*

Hi, I need our front-page redesigned. For the competition please submit a jpg of ABOVE THE FOLD ONLY. The full page redesign will be a revision request. URL is https://qp.trolvexa.hu/hu/index.html login:'fullhd' and password:'asdasd' (Fold is supposed to be at "Kiemelt Ajanlatok", use all elements above that. Please use at least one extra color other than the two in the logo, or you may completely change them. FOCUS should be on the central combined search box (3 dropdown, 2 calendar picker + Kereses Button) just like nestorly.com, ravimoto.com, Pelusi.com, etc... The search box is always large, central, white, we want that too. We want it to look more modern, more clean AND we want to feature a changing beautiful nature photo background (like nestorly.com).Please use our newly designed logo (in attached pdf) and use that new spelling: "ferntrail.online"

```html
<!DOCTYPE html>
<html lang="hu">
<head>
<meta charset="utf-8">
<title>ferntrail.online – Foglalj közvetlen a vadászterületnél</title>
<link href="https://fonts.googleapis.com/css2?family=Montserrat:wght@400;500;600&display=swap" rel="stylesheet">
<style>
  :root {
    --ink: #3d2a5c;
    --ink-dark: #33205e;
    --lavender: #f1e1fd;
    --white: #ffffff;
    --field-border: #b9b2c6;
    --accent: #f7c51a;
    --nav-muted: #cdbdf0;
    --topbar: #6543a6;
  }
  * { box-sizing: border-box; margin: 0; padding: 0; }
  html, body { width: 1200px; height: 675px; overflow: hidden; }
  body { font-family: 'Montserrat', sans-serif; color: var(--ink); position: relative; }

  .scenery {
    position: absolute; inset: 0;
    background:
      radial-gradient(ellipse 16% 22% at 87% 17%, rgba(150,120,200,.55), transparent 75%),
      radial-gradient(ellipse 14% 18% at 72% 22%, rgba(150,120,200,.45), transparent 75%),
      radial-gradient(ellipse 22% 18% at 88% 36%, rgba(236,140,185,.55), transparent 70%),
      radial-gradient(ellipse 20% 30% at 82% 70%, rgba(52,34,100,.85), transparent 72%),
      radial-gradient(ellipse 14% 30% at 7% 68%, rgba(50,32,96,.8), transparent 72%),
      radial-gradient(ellipse 22% 25% at 10% 40%, rgba(200,120,180,.45), transparent 72%),
      radial-gradient(ellipse 35% 12% at 50% 82%, rgba(110,110,240,.7), transparent 75%),
      linear-gradient(180deg, #563a9f 0%, #6c4aa8 28%, #9a6bb3 48%, #b57cb5 58%, #5a55c9 74%, #5c63e2 86%, #3b2f80 100%);
  }

  .topbar {
    position: absolute; left: 0; top: 0; width: 100%; height: 20px;
    background: var(--topbar);
  }
  .topbar .lang { position: absolute; left: 882px; top: 5px; display: flex; align-items: center; gap: 5px; }
  .flag { width: 18px; height: 10px; display: flex; flex-direction: column; }
  .flag span { flex: 1; }
  .topbar .divider { position: absolute; left: 923px; top: 2px; width: 1px; height: 17px; background: rgba(255,255,255,.35); }
  .topbar .currency { position: absolute; left: 932px; top: 4px; font-size: 9px; color: var(--nav-muted); display: flex; align-items: center; gap: 3px; }

  .site-header { position: absolute; left: 227px; top: 31px; width: 738px; height: 34px; }
  .brand { position: absolute; left: 0; top: 0; display: flex; align-items: center; gap: 6px; }
  .brand-dot { width: 34px; height: 34px; border-radius: 50%; background: var(--accent); }
  .brand-name { font-size: 15px; font-weight: 600; color: var(--white); }

  .main-nav { position: absolute; left: 307px; top: 11px; font-size: 10px; }
  .main-nav a { color: var(--nav-muted); text-decoration: none; position: absolute; white-space: nowrap; }
  .main-nav a.active { color: var(--white); }
  .partner-btn {
    position: absolute; left: 616px; top: 8px; width: 122px; height: 21px;
    background: var(--accent); color: var(--ink-dark); border-radius: 2px;
    font-size: 10px; display: flex; align-items: center; gap: 7px; padding-left: 6px; white-space: nowrap;
  }

  .search-card {
    position: absolute; left: 227px; top: 160px; width: 292px; height: 324px;
    background: var(--white); border-radius: 7px; overflow: hidden;
    box-shadow: 0 4px 18px rgba(40,20,80,.25);
  }
  .card-head { position: relative; height: 87px; background: var(--lavender); padding: 10px 14px 0; }
  .card-head h1 { font-size: 19px; font-weight: 600; line-height: 22px; color: var(--ink); }
  .card-head p { position: absolute; left: 14px; top: 68px; font-size: 10px; }
  .card-emblem { position: absolute; right: 16px; top: 13px; width: 39px; height: 39px; border-radius: 50%; background: var(--ink); }

  .field-label { position: absolute; font-size: 10px; }
  .select-box, .date-box {
    position: absolute; height: 18px; border: 1px solid var(--field-border); border-radius: 2px; background: var(--white);
  }
  .select-box .caret {
    position: absolute; right: 0; top: 0; width: 20px; height: 100%; border-left: 1px solid var(--field-border);
    display: flex; align-items: center; justify-content: center;
  }
  .date-box { display: flex; }
  .date-box .half { position: relative; flex: 1; }
  .date-box .half + .half { border-left: 1px solid var(--field-border); }
  .date-box svg { position: absolute; right: 4px; top: 3px; }

  .search-btn {
    position: absolute; left: 14px; top: 268px; width: 70px; height: 18px;
    background: var(--ink-dark); color: var(--white); border-radius: 2px;
    font-size: 10px; font-weight: 500; display: flex; align-items: center; justify-content: center;
  }
  .card-stats { position: absolute; left: 0; top: 305px; width: 100%; font-size: 5.5px; color: var(--ink); }
  .card-stats > * { position: absolute; top: 0; display: flex; align-items: center; gap: 2px; white-space: nowrap; }
  .card-stats a { color: var(--ink); text-decoration: underline; }
</style>
</head>
<body>
  <div class="scenery" role="img" aria-label="Illustrated evening landscape: purple mountains, pine trees, a winding river and a grazing deer"></div>

  <div class="topbar">
    <div class="lang">
      <div class="flag"><span style="background:#cd2a3e"></span><span style="background:#fff"></span><span style="background:#436f4d"></span></div>
      <svg width="9" height="6" viewBox="0 0 9 6"><path d="M1 1l3.5 3.5L8 1" fill="none" stroke="#cdbdf0" stroke-width="1"/></svg>
    </div>
    <div class="divider"></div>
    <div class="currency">EUR <svg width="9" height="6" viewBox="0 0 9 6"><path d="M1 1l3.5 3.5L8 1" fill="none" stroke="#cdbdf0" stroke-width="1"/></svg></div>
  </div>

  <header class="site-header">
    <div class="brand"><span class="brand-dot"></span><span class="brand-name">ferntrail.online</span></div>
    <nav class="main-nav">
      <a class="active" style="left:0">Országok</a>
      <a style="left:61px">Vadfajok</a>
      <a style="left:118px">Rólunk</a>
      <a style="left:168px">ÁSZF</a>
      <a style="left:209px">Hogyan működik</a>
    </nav>
    <div class="partner-btn">
      <svg width="12" height="10" viewBox="0 0 12 10"><circle cx="4" cy="3" r="2" fill="none" stroke="#33205e"/><path d="M0.5 9.5c0-2 1.5-3 3.5-3s3.5 1 3.5 3z" fill="none" stroke="#33205e"/><circle cx="8.5" cy="2.5" r="1.6" fill="none" stroke="#33205e"/><path d="M8 5.5c2 0 3.5.8 3.5 3" fill="none" stroke="#33205e"/></svg>
      Legyen partnerünk
    </div>
  </header>

  <section class="search-card">
    <div class="card-head">
      <h1>Nincs szükséged<br>vadászatszervezőre!</h1>
      <span class="card-emblem"></span>
      <p>Foglalj közvetlen a vadászterületnél</p>
    </div>

    <label class="field-label" style="left:14px;top:112px">Összes vad</label>
    <div class="select-box" style="left:14px;top:128px;width:114px"><span class="caret"><svg width="7" height="6" viewBox="0 0 7 6"><path d="M0 0h7L3.5 6z" fill="#33205e"/></svg></span></div>

    <label class="field-label" style="left:160px;top:112px">Összes ország</label>
    <div class="select-box" style="left:160px;top:128px;width:114px"><span class="caret"><svg width="7" height="6" viewBox="0 0 7 6"><path d="M0 0h7L3.5 6z" fill="#33205e"/></svg></span></div>

    <label class="field-label" style="left:14px;top:164px">Összes ajánlat</label>
    <div class="select-box" style="left:14px;top:180px;width:260px"><span class="caret"><svg width="7" height="6" viewBox="0 0 7 6"><path d="M0 0h7L3.5 6z" fill="#33205e"/></svg></span></div>

    <label class="field-label" style="left:14px;top:216px">Összes ajánlat</label>
    <div class="date-box" style="left:14px;top:232px;width:260px">
      <div class="half"><svg width="11" height="11" viewBox="0 0 11 11"><rect x=".5" y="1.5" width="10" height="9" fill="none" stroke="#a9a2b8"/><path d="M.5 3.5h10M3 5.5h1M5 5.5h1M7 5.5h1M3 7.5h1M5 7.5h1M7 7.5h1" stroke="#a9a2b8"/></svg></div>
      <div class="half"><svg width="11" height="11" viewBox="0 0 11 11"><rect x=".5" y="1.5" width="10" height="9" fill="none" stroke="#a9a2b8"/><path d="M.5 3.5h10M3 5.5h1M5 5.5h1M7 5.5h1M3 7.5h1M5 7.5h1M7 7.5h1" stroke="#a9a2b8"/></svg></div>
    </div>

    <div class="search-btn">Kereses</div>

    <div class="card-stats">
      <span style="left:14px"><svg width="4" height="5" viewBox="0 0 4 5"><path d="M2 5C.5 3 0 2.4 0 2a2 2 0 014 0c0 .4-.5 1-2 3z" fill="#3d2a5c"/></svg>123456 terület</span>
      <span style="left:70px"><svg width="5" height="5" viewBox="0 0 5 5"><circle cx="2.5" cy="2.5" r="1.7" fill="none" stroke="#3d2a5c" stroke-width=".8"/><path d="M2.5 0v5M0 2.5h5" stroke="#3d2a5c" stroke-width=".6"/></svg>87654321 ajánlat</span>
      <a style="left:133px">Részletes</a>
    </div>
  </section>
</body>
</html>
```